Stationary set for consulting company
Tarvo Bridge
Creative Brief
Modern
Karim Yusuf Al Banna
Co-Founder
Reef Spire, Abu Dhabi United Arab Emirates
karim@tarvobridge.ae
www.tarvobridge.com
I need a full stationary set for the company logo I will be attaching. (PPTs, business cards, envelope, letterhead, etc)

```html
<!DOCTYPE html>
<html lang="en">
<head>
<meta charset="utf-8">
<title>Tarvo Bridge Stationery Set</title>
<link href="https://fonts.googleapis.com/css2?family=Montserrat:wght@500;700;800&display=swap" rel="stylesheet">
<style>
  :root {
    --navy: #26428b;
    --sky: #a8c6ea;
    --paper: #ffffff;
    --backdrop: #e4e5e7;
    --ink: #26428b;
  }
  * { margin: 0; padding: 0; box-sizing: border-box; }
  html, body { width: 1200px; height: 629px; overflow: hidden; }
  body { background: var(--backdrop); font-family: "Montserrat", sans-serif; color: var(--ink); position: relative; }
  .piece { position: absolute; background: var(--paper); overflow: hidden; box-shadow: 0 1px 3px rgba(0,0,0,.12); }
  .piece svg.band { position: absolute; left: 0; width: 100%; display: block; }
  .brand { display: flex; align-items: center; gap: 5px; font-weight: 800; color: var(--navy); white-space: nowrap; text-transform: uppercase; letter-spacing: .02em; }
  .brand .mark { background: var(--navy); flex: none; }
  .brand.light { color: var(--paper); }
  .brand.light .mark { background: var(--paper); }
  .fine { font-weight: 500; white-space: nowrap; text-align: center; }

  /* business cards */
  .card-front { left: 48px; top: 101px; width: 144px; height: 72px; }
  .card-front .mark-small { position: absolute; left: 62px; top: 16px; width: 16px; height: 14px; border: 2px solid var(--navy); }
  .card-front .name { position: absolute; left: 0; right: 0; top: 38px; font-size: 5px; font-weight: 700; }
  .card-front .role { position: absolute; left: 0; right: 0; top: 45px; font-size: 3.5px; }
  .card-back { left: 209px; top: 101px; width: 144px; height: 72px; background: var(--navy); display: flex; align-items: center; justify-content: center; }
  .card-back .brand { font-size: 10px; }
  .card-back .mark { width: 9px; height: 9px; }

  /* envelope */
  .envelope-front { left: 48px; top: 230px; width: 305px; height: 144px; }
  .envelope-front .brand { position: absolute; left: 12px; top: 12px; font-size: 9px; }
  .envelope-front .mark { width: 8px; height: 8px; }
  .envelope-front .band { top: 90px; height: 30px; }
  .envelope-front .band-text { position: absolute; left: 0; right: 0; top: 108px; font-size: 4px; color: var(--paper); }
  .envelope-back { left: 48px; top: 396px; width: 305px; height: 156px; }
  .envelope-back svg { position: absolute; inset: 0; width: 100%; height: 100%; }

  /* letterhead */
  .letterhead { left: 377px; top: 101px; width: 343px; height: 461px; }
  .letterhead .brand { position: absolute; left: 0; right: 0; top: 18px; justify-content: center; font-size: 11px; }
  .letterhead .mark { width: 10px; height: 10px; }
  .letterhead .band { top: 400px; height: 61px; }
  .letterhead .footer { position: absolute; left: 0; right: 0; top: 426px; font-size: 4.5px; color: var(--paper); line-height: 1.6; }

  /* presentation folder */
  .folder { left: 751px; top: 91px; width: 411px; height: 466px; background: var(--sky); box-shadow: none; }
  .folder svg { position: absolute; inset: 0; width: 100%; height: 100%; }
  .folder .brand { position: absolute; left: 240px; top: 110px; font-size: 13px; }
  .folder .mark { width: 12px; height: 12px; }
  .folder .band-text { position: absolute; left: 20px; width: 184px; top: 272px; font-size: 3.6px; color: var(--paper); line-height: 1.7; }
</style>
</head>
<body>

  <div class="piece card-front">
    <span class="mark-small"></span>
    <p class="fine name">Karim Yusuf Al Banna</p>
    <p class="fine role">Co-Founder</p>
  </div>

  <div class="piece card-back">
    <div class="brand light"><span class="mark"></span>Tarvo Bridge</div>
  </div>

  <div class="piece envelope-front">
    <div class="brand"><span class="mark"></span>Tarvo Bridge</div>
    <svg class="band" viewBox="0 0 305 30" preserveAspectRatio="none" aria-hidden="true">
      <polygon points="0,12 305,12 305,26 0,26" fill="var(--navy)"/>
      <polygon points="0,0 12,0 0,12" fill="var(--navy)"/>
      <polygon points="276,0 305,0 305,8 284,8" fill="var(--navy)"/>
    </svg>
    <p class="fine band-text">Reef Spire, Abu Dhabi, United Arab Emirates</p>
  </div>

  <div class="piece envelope-back">
    <svg viewBox="0 0 305 156" preserveAspectRatio="none" aria-hidden="true">
      <rect width="305" height="156" fill="var(--paper)"/>
      <polygon points="0,0 305,0 305,14 152,62 0,14" fill="var(--navy)"/>
      <polyline points="0,22 152,70 305,22" fill="none" stroke="var(--navy)" stroke-width="1"/>
    </svg>
  </div>

  <div class="piece letterhead">
    <div class="brand"><span class="mark"></span>Tarvo Bridge</div>
    <svg class="band" viewBox="0 0 343 61" preserveAspectRatio="none" aria-hidden="true">
      <polygon points="40,10 343,10 343,61 0,61 0,36" fill="var(--navy)"/>
      <polygon points="0,20 26,0 32,0 0,26" fill="var(--navy)"/>
    </svg>
    <div class="fine footer">
      <p>Reef Spire, Abu Dhabi United Arab Emirates</p>
      <p>Tel: +971 2 555 0142 | karim@tarvobridge.ae | www.tarvobridge.com</p>
    </div>
  </div>

  <div class="piece folder">
    <svg viewBox="0 0 411 466" preserveAspectRatio="none" aria-hidden="true">
      <rect x="19" y="0" width="373" height="268" fill="var(--paper)"/>
      <line x1="205" y1="0" x2="205" y2="268" stroke="#dfe3ea" stroke-width="1"/>
      <polygon points="0,257 411,257 411,307 0,307" fill="var(--navy)"/>
      <polygon points="372,246 382,246 411,276 411,290" fill="var(--navy)"/>
      <rect x="19" y="307" width="373" height="159" fill="var(--sky)"/>
      <path d="M150,345 q-12,40 0,80" fill="none" stroke="var(--navy)" stroke-width="1.2"/>
      <path d="M261,345 q12,40 0,80" fill="none" stroke="var(--navy)" stroke-width="1.2"/>
      <line x1="205" y1="307" x2="205" y2="466" stroke="#8fb1dd" stroke-width="1"/>
    </svg>
    <div class="brand"><span class="mark"></span>Tarvo Bridge</div>
    <div class="fine band-text">
      <p>Reef Spire, Abu Dhabi United Arab Emirates</p>
      <p>Tel: +971 2 555 0142 | www.tarvobridge.com</p>
    </div>
  </div>

</body>
</html>
```